Small chamber of commerce in upstate new york. Need basic design to announce a new chocolate festival that will intend to bring in tourists to our area and give our local merchants exposure.

Industry/Entity Type

Chamber Of Commerce

Requirements
Must have
• (Beyond the information that has been listed on the enclosed jpeg, I would like to have some details on the reverse side that would include:)

Cooking with Chocolate Demo
Chocolate Decorating competition with Kids/Pastry Chefs
Live Music
Fudge Rocket Scooter Sprint
Lots & Lots of Chocolate!!!

More information contact info@pinevalechamber.org or call 845.555.0147.

```html
<!DOCTYPE html>
<html lang="en">
<head>
<meta charset="utf-8">
<title>Chocolate Festival – Event Highlights</title>
<link rel="stylesheet" href="https://fonts.googleapis.com/css2?family=Source+Sans+3:wght@300;400&display=swap">
<style>
  :root {
    --page: #ffffff;
    --card: #d4c4b9;
    --text: #2b2523;
    --text-strong: #141111;
    --bullet: #e0101a;
    --ornament: #8a5a3c;
  }
  * { margin: 0; padding: 0; box-sizing: border-box; }
  html, body {
    width: 1200px;
    height: 930px;
    overflow: hidden;
    background: var(--page);
  }
  .flyer-back {
    position: absolute;
    left: 30px;
    top: 30px;
    width: 1140px;
    height: 870px;
    background: var(--card);
    font-family: "Source Sans 3", "Myriad Pro", sans-serif;
    font-weight: 300;
    color: var(--text);
    text-align: center;
  }
  .highlights {
    list-style: none;
    position: absolute;
    top: 155px;
    left: 0;
    width: 100%;
    font-size: 33px;
    line-height: 40px;
  }
  .highlights li { margin-bottom: 24px; }
  .highlights li::before {
    content: "•";
    color: var(--bullet);
    margin-right: 8px;
    font-size: 26px;
    vertical-align: 2px;
  }
  .highlights .sponsor {
    font-weight: 400;
    color: var(--text-strong);
  }
  .highlights .contact { line-height: 40px; }
  .ornament {
    position: absolute;
    left: 485px;
    top: 671px;
    width: 170px;
    height: 32px;
    background: var(--ornament);
    border-radius: 16px;
    opacity: 0.85;
  }
</style>
</head>
<body>
  <section class="flyer-back">
    <ul class="highlights">
      <li>Cooking with Chocolate Demo</li>
      <li>Chocolate Decorating competition with Kids/Pastry Chefs</li>
      <li>Live Music</li>
      <li>Fudge Rocket Scooter Sprint</li>
      <li>Lots &amp; Lots of Chocolate!!!</li>
      <li class="sponsor">Sponsorships now available</li>
      <li class="contact">More information contact info@pinevalechamber.org or<br>call 845.555.0147.</li>
    </ul>
    <div class="ornament" role="img" aria-label="Decorative brown flourish divider"></div>
  </section>
</body>
</html>
```